Brochure, Stationary and Card Design for Machining and Manufacturing

Keystone Fabrication Inc. requires a package of stationary including a Tri-Fold and Pocket Folder Brochure, Business Card and Letterhead based on the existing branding from our website design and logo.

Keystone Fabrication is a Machine Shop located in Western Canada that specializes in CNC Machining, Electrical Discharge Machining and Rapid Repair Services. Our products are diverse and technically advanced in the oilfield industry. Our Competition is Pellet, Vireo, and Brantwell Oil Tools and the website links are below for your review. Attached is our Website design, logo, pictures, competitor brochures and brochure copy

Our design should be high-tech, professional and should resemble superior quality and customer services. Our website is designed with a HD background picture and we use semi-transparent text boxes to display smaller photos, titles and text. We would like mostly white text and the teal titles as per the colour in the logo. We want a product that can be updated as we make changes to our services by using Photoshop or similar software.

Branding needs to be shared between all the products. Please see our photos and documents attached for inspiration. We will monitor feedback and questions to direct everyone in the right direction.

Attached:

- Pictures to use for background and Titled sections with content. Content to be uploaded soon.
- Sample of existing business card. Add the ISO image to the new card. Brand an all new card from all information.
- Copy of our website design. This is the main inspiration to build around. This site is under construction right now.

www.brantwelloiltools.example **Sample Pics for front of brochure. I like this pic. I will upload pics of our manager like this for you to use to build something inspired by this pic.

www.pelletmachine.example

www.vireomachine.example **Attached a 2 copies of a sample brochure of this competitor.

Target Market(s)

Industrial Purchasers of machining and manufacturing in the oil and gas industry. Down-Hole oil tools, drilling tools, Hydraulic Fracturing and Well Completions.

Industry/Entity Type

Construction

Requirements
Must have
• Business Contact Info:

Keystone Fabrication Inc.
4362-17 Ave NW
Edmonton, AB, T9K 2R4
T: (780) 555-0147
F: (888) 555-0192
Email: info@keystonefab.example

Please add: "ISO 9001-2008 Certification" as part of the logo, text, or the Tellmark ISO image to all items.
Nice to have
• All pictures need touch up and lighting to be corrected. Image 0090 is dark/yellow and needs to be adjusted to be similar colour to other pics.
Should not have
• No background picture on the business card. Keep the card more simplified and clean. Please use the attached ISO logo for the card as well.

```html
<!DOCTYPE html>
<html lang="en">
<head>
<meta charset="utf-8">
<title>Keystone Fabrication – Business Card</title>
<link rel="stylesheet" href="https://fonts.googleapis.com/css2?family=Open+Sans:wght@400;600;700;800&display=swap">
<style>
  :root {
    --page-bg: #ececec;
    --card-bg: #ffffff;
    --ink: #1a1a1a;
    --ink-soft: #3a3a3a;
    --teal: #1b95a3;
    --teal-mark: #2fa9b6;
  }
  * { box-sizing: border-box; margin: 0; padding: 0; }
  html, body {
    width: 1200px;
    height: 848px;
    overflow: hidden;
    background: var(--page-bg);
    font-family: "Open Sans", Arial, sans-serif;
  }
  .sheet {
    position: relative;
    width: 1200px;
    height: 848px;
  }
  .card {
    position: absolute;
    top: 276px;
    width: 520px;
    height: 297px;
    background: var(--card-bg);
    box-shadow: 0 6px 18px rgba(0,0,0,0.22);
  }
  .card--back { left: 50px; }
  .card--front { left: 630px; }

  .brand {
    position: absolute;
    display: flex;
    align-items: center;
    gap: 10px;
  }
  .card--back .brand { left: 44px; top: 118px; }
  .card--front .brand { left: 44px; top: 92px; }
  .brand__square {
    width: 40px;
    height: 40px;
    background: var(--teal-mark);
  }
  .brand__name {
    font-weight: 800;
    font-size: 27px;
    letter-spacing: -0.3px;
    color: var(--ink);
    text-transform: uppercase;
    line-height: 1;
  }

  .contact {
    position: absolute;
    left: 262px;
    top: 160px;
    width: 240px;
  }
  .contact__name {
    font-weight: 700;
    font-size: 19px;
    letter-spacing: 0.5px;
    color: var(--ink);
    line-height: 1.05;
  }
  .contact__company {
    font-size: 10px;
    color: var(--teal);
    line-height: 1.25;
    margin-top: 2px;
  }
  .contact__address {
    font-size: 10px;
    color: var(--ink-soft);
    line-height: 1.2;
  }
  .contact__lines {
    list-style: none;
    margin-top: 6px;
    margin-left: -16px;
  }
  .contact__line {
    display: flex;
    align-items: center;
    gap: 6px;
    font-weight: 600;
    font-size: 12px;
    color: var(--teal);
    line-height: 1.45;
  }
  .contact__icon {
    width: 11px;
    height: 11px;
    flex: none;
    fill: var(--ink);
  }
</style>
</head>
<body>
<main class="sheet">

  <section class="card card--back" aria-label="Business card back">
    <div class="brand">
      <span class="brand__square"></span>
      <span class="brand__name">Keystone Fabrication</span>
    </div>
  </section>

  <section class="card card--front" aria-label="Business card front">
    <div class="brand">
      <span class="brand__square"></span>
      <span class="brand__name">Keystone Fabrication</span>
    </div>

    <div class="contact">
      <p class="contact__name">JOHN DOE</p>
      <p class="contact__company">Keystone Fabrication Inc.</p>
      <p class="contact__address">4362-17 Ave NW<br>Edmonton, AB, T9K 2R4</p>
      <ul class="contact__lines">
        <li class="contact__line">
          <svg class="contact__icon" viewBox="0 0 12 12" aria-hidden="true">
            <path d="M1 3.5C1 2 2.5 1.5 6 1.5S11 2 11 3.5V4.5H8.5V3.5H3.5V4.5H1Z"/>
            <rect x="2.5" y="5" width="7" height="5.5" rx="1"/>
          </svg>
          T: (780) 555-0147
        </li>
        <li class="contact__line">
          <svg class="contact__icon" viewBox="0 0 12 12" aria-hidden="true">
            <rect x="3" y="1" width="6" height="3.5"/>
            <rect x="1" y="5" width="10" height="5.5" rx="1"/>
          </svg>
          F: (888) 555-0192
        </li>
        <li class="contact__line">
          <svg class="contact__icon" viewBox="0 0 12 12" aria-hidden="true">
            <path d="M1 3H11V10H1Z M1.6 3.4L6 7L10.4 3.4" stroke="#fff" stroke-width="0.8"/>
          </svg>
          Email: info@keystonefab.example
        </li>
      </ul>
    </div>
  </section>

</main>
</body>
</html>
```